Anzeigengestaltung für Online-Handel mit Edelmetallen
Zielgruppe
Online Handel mit Edelmetallen wie Gold und Silberbarren und Münzen.
Sowie der Ankauf von Gold per Postankauf
Aufgabenstellung
Ich möchte in verschiedenen Tageszeitungen in Deutschland Werbung schalten . Kleine Anzeigen etwas kleiner als Visitenkarten Größe wegen den Kosten.
Logo
Ihr Onlineshop für Edelmetalle
Vergleichen sie unsere Preis
Goldbarren / Falkenthaler
Shop.Wertkontorlo.de

```html
<!DOCTYPE html>
<html lang="de">
<head>
<meta charset="utf-8">
<title>Anzeige – Onlineshop für Edelmetalle</title>
<link rel="stylesheet" href="https://fonts.googleapis.com/css2?family=Fraunces:opsz,wght@9..144,600&family=Bebas+Neue&family=Poppins:wght@300;500&display=swap">
<style>
  :root {
    --page-bg: #efeeee;
    --ad-bg: #373739;
    --gold: #d1a04a;
    --gold-light: #e6bd4a;
    --gold-deep: #b5842c;
    --white: #ffffff;
  }
  html, body {
    margin: 0;
    width: 1200px;
    height: 1200px;
    overflow: hidden;
    background: var(--page-bg);
  }
  .ad {
    position: absolute;
    left: 125px;
    top: 198px;
    width: 960px;
    height: 812px;
    background: var(--ad-bg);
    overflow: hidden;
  }
  .ad-art {
    position: absolute;
    inset: 0;
    width: 960px;
    height: 812px;
  }
  .headline {
    position: absolute;
    left: 58px;
    top: 52px;
    margin: 0;
    font-family: "Fraunces", Georgia, serif;
    font-weight: 600;
    font-size: 60px;
    line-height: 86px;
    color: var(--white);
    letter-spacing: 0.5px;
  }
  .price-badge-text {
    position: absolute;
    left: 639px;
    top: 108px;
    width: 300px;
    margin: 0;
    text-align: center;
    font-family: "Bebas Neue", "Arial Narrow", sans-serif;
    font-size: 50px;
    line-height: 56px;
    color: var(--white);
    transform: rotate(4deg);
  }
  .brand-name {
    position: absolute;
    left: 56px;
    top: 722px;
    margin: 0;
    font-family: "Poppins", Arial, sans-serif;
    font-weight: 300;
    font-size: 30px;
    line-height: 30px;
    color: var(--white);
  }
  .shop-button {
    position: absolute;
    left: 425px;
    top: 660px;
    width: 512px;
    height: 68px;
    border-radius: 14px;
    background: var(--gold);
    color: var(--white);
    font-family: "Poppins", Arial, sans-serif;
    font-weight: 500;
    font-size: 34px;
    line-height: 68px;
    text-align: center;
  }
</style>
</head>
<body>
  <div class="ad">
    <svg class="ad-art" viewBox="0 0 960 812" xmlns="http://www.w3.org/2000/svg">
      <defs>
        <linearGradient id="photoTone" x1="0" y1="0" x2="0" y2="1">
          <stop offset="0" stop-color="var(--gold-light)"/>
          <stop offset="1" stop-color="var(--gold-deep)"/>
        </linearGradient>
      </defs>
      <path class="photo-area" role="img" aria-label="Foto: Stapel aus Goldbarren mit einem großen Feingold-Barren in der Mitte"
            fill="url(#photoTone)"
            d="M0,334 H960 V518 Q480,622 0,494 Z"/>
      <path class="gold-swoosh" d="M0,505 Q480,650 960,531" fill="none" stroke="var(--gold)" stroke-width="4"/>
      <circle class="price-badge" cx="789" cy="195" r="157" fill="var(--gold)"/>
      <circle class="price-badge-ring" cx="789" cy="195" r="142" fill="none" stroke="var(--white)" stroke-width="3"/>
    </svg>

    <h1 class="headline">Ihr Onlineshop<br>für Edelmetalle</h1>
    <p class="price-badge-text">Vergleichen<br>Sie unsere<br>Preis!</p>
    <p class="brand-name">Wertkontor-Lo.de</p>
    <div class="shop-button">Shop.Wertkontorlo.de</div>
  </div>
</body>
</html>
```